Business Cards Needed For Veterinary Business

Looking for a business card design for a veterinary blood bank. We would like it to be clean and professional on appearance but still warm and inviting. We would like to utilize our logo and similar coloring. We will use our phone number, email, website, employee name, employee title.

We do not want a bunch of animated animal photos but do not need the style to be as clinical as a laboratory or human medical procedure office.

We are looking for some creative ideas to choose from so that we can generate a standout professional business card for our management team to utilize.

Target Market(s)

professionals

Industry/Entity Type

veterinary

Contact Information for Business Card

employee name, employee title, phone number, website URL, email

Font styles to use
Sans Serif

Colors
0054AA
0677BA
7BADD7
CADEEF
E8F1F8
EB3D1F
EC4F4E
F09395
F8D3D4
FCEDEE

Requirements
Nice to have
• creative design
Should not have
• animated photos

```html
<!DOCTYPE html>
<html lang="en">
<head>
<meta charset="utf-8">
<title>HVBC Business Card</title>
<link rel="stylesheet" href="https://fonts.googleapis.com/css2?family=Montserrat:ital,wght@0,400;0,700;1,400&display=swap">
<style>
  :root {
    --stage: #0d2766;
    --paper: #ffffff;
    --brand-red: #e81d25;
    --ink-grey: #6b6b6b;
    --rule-grey: #d4d4d4;
  }
  * { margin: 0; padding: 0; box-sizing: border-box; }
  html, body {
    width: 1200px;
    height: 1145px;
    overflow: hidden;
    background: var(--stage);
    font-family: "Montserrat", sans-serif;
  }
  .stage {
    position: relative;
    width: 1200px;
    height: 1145px;
  }
  .card {
    position: absolute;
    left: 160px;
    width: 880px;
    height: 503px;
    background: var(--paper);
    overflow: hidden;
    box-shadow: 0 10px 30px rgba(0,0,0,0.35);
  }
  .card--front { top: 46px; }
  .card--back  { top: 596px; }

  .card__accent {
    position: absolute;
    background: var(--brand-red);
  }
  .card__accent--top {
    left: 0;
    top: 0;
    width: 210px;
    height: 142px;
  }
  .card__accent--bottom {
    right: 0;
    bottom: 0;
    width: 170px;
    height: 128px;
  }

  .brand-name {
    position: absolute;
    display: flex;
    align-items: center;
    color: var(--brand-red);
    font-weight: 700;
    letter-spacing: 0.5px;
  }
  .brand-name__dot {
    display: block;
    border-radius: 50%;
    background: var(--brand-red);
  }
  .card--front .brand-name { left: 132px; top: 232px; font-size: 44px; gap: 12px; }
  .card--front .brand-name__dot { width: 40px; height: 40px; }
  .card--back .brand-name { left: 0; right: 0; justify-content: center; top: 210px; font-size: 72px; gap: 18px; }
  .card--back .brand-name__dot { width: 62px; height: 62px; }

  .divider {
    position: absolute;
    left: 466px;
    top: 207px;
    width: 2px;
    height: 133px;
    background: var(--rule-grey);
  }
  .person {
    position: absolute;
    left: 524px;
    top: 172px;
  }
  .person__name {
    color: var(--brand-red);
    font-weight: 700;
    font-size: 35px;
    line-height: 1;
  }
  .person__title {
    color: var(--ink-grey);
    font-style: italic;
    font-size: 16px;
    margin-top: 6px;
  }
  .contact {
    position: absolute;
    left: 524px;
    top: 252px;
    list-style: none;
  }
  .contact__item {
    display: flex;
    align-items: center;
    height: 22px;
    margin-bottom: 24px;
    color: var(--ink-grey);
    font-size: 18px;
  }
  .contact__icon {
    width: 18px;
    height: 18px;
    margin-right: 19px;
    fill: var(--brand-red);
    stroke: var(--brand-red);
  }
</style>
</head>
<body>
<main class="stage">

  <section class="card card--front" aria-label="Card front">
    <div class="card__accent card__accent--top" role="img" aria-label="Red splash decoration"></div>
    <div class="card__accent card__accent--bottom" role="img" aria-label="Red splash decoration"></div>

    <div class="brand-name"><span class="brand-name__dot"></span>HVBC</div>
    <div class="divider"></div>

    <div class="person">
      <p class="person__name">Daniel Reyes</p>
      <p class="person__title">General Manager</p>
    </div>

    <ul class="contact">
      <li class="contact__item">
        <svg class="contact__icon" viewBox="0 0 24 24" aria-hidden="true"><path stroke="none" d="M6.6 10.8a15.1 15.1 0 0 0 6.6 6.6l2.2-2.2c.3-.3.7-.4 1-.2 1.1.4 2.3.6 3.6.6.6 0 1 .4 1 1V20c0 .6-.4 1-1 1A17 17 0 0 1 3 4c0-.6.4-1 1-1h3.5c.6 0 1 .4 1 1 0 1.3.2 2.5.6 3.6.1.3 0 .7-.2 1z"/></svg>
        +1 (000) 123-1234
      </li>
      <li class="contact__item">
        <svg class="contact__icon" viewBox="0 0 24 24" aria-hidden="true"><circle cx="12" cy="12" r="4" fill="none" stroke-width="2.2"/><path fill="none" stroke-width="2.2" d="M16 12v1.5a2.5 2.5 0 0 0 5 0V12a9 9 0 1 0-3.6 7.2"/></svg>
        name@website.com
      </li>
      <li class="contact__item">
        <svg class="contact__icon" viewBox="0 0 24 24" aria-hidden="true"><circle cx="12" cy="12" r="9.5" fill="none" stroke-width="2"/><path fill="none" stroke-width="1.6" d="M2.5 12h19M12 2.5c3 3 3 16 0 19M12 2.5c-3 3-3 16 0 19M4.5 7h15M4.5 17h15"/></svg>
        www.website.com
      </li>
    </ul>
  </section>

  <section class="card card--back" aria-label="Card back">
    <div class="card__accent card__accent--top" role="img" aria-label="Red splash decoration"></div>
    <div class="card__accent card__accent--bottom" role="img" aria-label="Red splash decoration"></div>

    <div class="brand-name"><span class="brand-name__dot"></span>HVBC</div>
  </section>

</main>
</body>
</html>
```